metal roofing website

I have several domain names and a website that has been built. I need someone to recreate essentially the same website and change some photos and basic design to create the new sites. I have all of the files and c panel access to the lucky winner. If you can do a good job at a fair price I will have 100's of sites to send to you very soon. I have the site built and have all files just need it recreated on my server. the current site is www.dorvanemetalinc.com I am looking to get this done ASAP!!!

```html
<!DOCTYPE html>
<html lang="en">
<head>
<meta charset="utf-8">
<title>Dorvane Metal Inc – Roofing</title>
<link href="https://fonts.googleapis.com/css2?family=Lato:wght@400;700;900&display=swap" rel="stylesheet">
<style>
:root{
  --red:#b7302a;
  --red-dark:#9e2520;
  --ink:#111;
  --text:#333;
  --muted:#666;
  --topbar:#f4f4f4;
  --sand:#d8cebf;
  --footer:#1c1c1c;
  --white:#fff;
}
*{box-sizing:border-box;margin:0;padding:0}
html,body{width:1200px;height:2293px;overflow:hidden}
body{font-family:'Lato',sans-serif;color:var(--text);background:var(--white);position:relative}
.abs{position:absolute}

/* top bar */
.topbar{top:0;left:0;width:1200px;height:37px;background:var(--topbar)}
.topbar .tagline{left:220px;top:11px;font-size:11px;font-weight:700;color:var(--ink)}
.topbar .links{right:215px;top:0;display:flex;height:37px;font-size:11px;font-weight:700;color:var(--ink)}
.topbar .links span{padding:0 11px;line-height:37px}
.topbar .links .city{background:#dcdcdc}

/* header */
.brand{left:222px;top:60px;display:flex;align-items:center;gap:8px}
.brand .mark{width:22px;height:22px;background:var(--red)}
.brand .name{font-size:22px;font-weight:900;color:var(--red);line-height:1}
.contact-blocks{left:578px;top:66px;display:flex}
.cblock{display:flex;gap:10px;padding:0 20px;border-left:1px solid #ddd;font-size:11px}
.cblock:first-child{border-left:none}
.cblock b{display:block;color:var(--ink);font-size:11px}
.cblock small{color:#888;font-size:10px;line-height:1.3;display:block}
.cblock svg{width:20px;height:20px;flex:none;margin-top:2px}

/* nav */
.nav{left:220px;top:133px;width:760px;height:32px;background:var(--red);display:flex;align-items:center;padding-left:14px}
.nav a{color:var(--white);font-size:11px;font-weight:700;text-decoration:none;margin-right:19px}
.nav a.current{font-weight:400}
.nav .social{margin-left:auto;display:flex;gap:4px;margin-right:4px}
.nav .social i{width:22px;height:22px;background:var(--red-dark);border:1px solid #d9645e;display:block}

/* hero */
.hero{top:165px;left:0;width:1200px;height:587px;background:linear-gradient(180deg,#6f7478 0%,#8a8c86 35%,#7e7a6a 55%,#4f6a33 75%,#3d5a26 100%)}
.hero h1{left:0;width:1200px;top:386px;text-align:center;color:var(--white);font-size:42px;font-weight:700;line-height:.95}
.btn{height:31px;border-radius:4px;font-size:14px;font-weight:700;color:var(--white);display:flex;align-items:center;justify-content:center}
.btn-red{left:477px;top:488px;width:113px;background:var(--red)}
.btn-line{left:610px;top:488px;width:113px;border:2px solid var(--white)}
.slider-nav{left:1174px;top:408px;width:20px;display:flex;flex-direction:column;align-items:center;gap:8px}
.slider-nav i{width:6px;height:6px;border-radius:50%;background:#111;display:block}
.slider-nav i.on{background:var(--red)}

/* roofing */
.worker{left:107px;top:688px;width:145px;height:260px;background:linear-gradient(180deg,#d7b23a 0%,#c9d4de 25%,#a9b9c7 70%,#efefef 100%);border-radius:40px 40px 6px 6px}
.roofing-title{left:277px;top:795px;font-size:15px;font-weight:700;color:var(--ink)}
.roofing-rule{left:277px;top:818px;width:108px;height:3px;background:var(--red)}
.roofing-dots{left:387px;top:818px;width:10px;height:3px;background:radial-gradient(circle,#111 1.5px,transparent 2px) 0 0/5px 3px}
.roofing-sub{left:277px;top:831px;font-size:10px;color:var(--ink)}
.service{top:858px;width:220px;text-align:center}
.service svg{width:52px;height:48px;display:block;margin:0 auto 10px}
.service p{font-size:13px;font-weight:700;color:var(--ink)}

/* call band */
.callband{top:971px;left:0;width:1200px;height:102px;background:var(--sand)}
.callband p{left:348px;top:38px;font-size:20px;font-weight:700;color:var(--red);word-spacing:1px}
.callband .num{left:731px}

/* gallery */
.section-title{font-size:20px;font-weight:900;color:var(--ink)}
.section-title em{font-style:normal;color:var(--red)}
.gallery-title{left:0;width:1200px;top:1091px;text-align:center}
.tabs{left:344px;top:1140px;width:513px;height:30px;background:#111;border-radius:5px;display:flex;overflow:hidden}
.tabs span{color:var(--white);font-size:13px;font-weight:700;line-height:30px;padding:0 18px}
.tabs span.on{background:var(--red);padding:0 24px}
.shots{left:0;top:1214px;width:1200px;height:292px;display:flex;gap:2px}
.shot{flex:1;height:292px}
.shot-1{background:linear-gradient(180deg,#c8ccd0 0%,#3b2e2c 30%,#c7a57a 55%,#4a8a35 80%)}
.shot-2{background:linear-gradient(180deg,#7c7f80 0%,#4a3b36 30%,#b79a73 55%,#625048 85%)}
.shot-3{background:linear-gradient(180deg,#d6d8da 0%,#b9bbbd 45%,#e4e2de 55%,#8c7b6a 75%)}
.shot-4{background:linear-gradient(180deg,#d2d4d6 0%,#7a2b30 30%,#e6d8b8 50%,#9b9896 80%)}
.pager{width:120px;height:20px;display:flex;align-items:center;justify-content:center;gap:6px}
.pager i{width:5px;height:5px;border-radius:50%;background:#111;display:block}
.pager i.on{background:var(--red)}
.pager svg{width:12px;height:16px;margin:0 10px}
.pager-gallery{left:540px;top:1541px}

/* testimonials */
.testimonials{top:1598px;left:0;width:1200px;height:345px;background:var(--sand)}
.testimonials .section-title{left:222px;top:32px;font-size:19px}
.quote{top:82px;width:369px;height:126px;background:var(--white);border:2px solid #c5c5c5;box-shadow:0 1px 3px rgba(0,0,0,.2);padding:14px 16px;font-size:11px;line-height:1.6;text-align:center;color:var(--ink)}
.quote::after{content:"";position:absolute;left:-2px;bottom:-16px;border-top:14px solid var(--red);border-right:14px solid transparent}
.author{top:225px;display:flex;align-items:center;gap:10px;font-size:11px;color:var(--ink)}
.author .avatar{width:50px;height:50px;border-radius:50%;background:radial-gradient(circle,#9c8f86 40%,#f2f2f2 42%)}
.author b{color:var(--red);font-weight:700}
.pager-quotes{left:540px;top:295px}

/* footer */
.footer{top:1943px;left:0;width:1200px;height:350px;background:linear-gradient(180deg,#2a2a2a,#141414)}
.footer .brand-foot{left:300px;top:58px;font-size:20px;font-weight:900;color:#e0e0e0;display:flex;align-items:center;gap:8px}
.footer .brand-foot i{width:18px;height:18px;background:#9a9a9a;display:block}
.footer .about{left:220px;top:141px;width:225px;font-size:10.5px;line-height:1.75;color:#ddd;text-align:center}
.fcol h4{font-size:14px;font-weight:700;color:var(--white);margin-bottom:10px}
.fcol p{font-size:9.5px;color:#eee;line-height:1.95}
.fcol-touch{left:544px;top:40px}
.fcol-hours{left:544px;top:140px}
.fcol-news{left:743px;top:40px}
.newsletter{left:743px;top:98px;width:237px;height:34px;display:flex;border:1px solid #bbb}
.newsletter span{flex:1;font-size:10px;color:#aaa;line-height:32px;padding-left:12px;background:#111}
.newsletter b{width:46px;background:var(--red);color:var(--white);font-size:11px;text-align:center;line-height:32px}
.footer .rule{left:309px;top:291px;width:582px;height:1px;background:#bbb}
.footer .flinks{left:0;width:1200px;top:305px;text-align:center;font-size:10px;font-weight:700;color:var(--white);word-spacing:10px}
.footer .copy{left:0;width:1200px;top:327px;text-align:center;font-size:7px;color:#ccc}
</style>
</head>
<body>

<header>
  <div class="abs topbar">
    <p class="abs tagline">Dorvane Metal Manufacturers of quality Building Components</p>
    <nav class="abs links"><span>Faq</span><span>Shop</span><span>BuyNow</span><span class="city">NewYork</span></nav>
  </div>

  <div class="abs brand"><span class="mark"></span><span class="name">DORVANE METAL</span></div>

  <div class="abs contact-blocks">
    <div class="cblock">
      <svg viewBox="0 0 24 24" fill="none" stroke="#999" stroke-width="1.6"><path d="M5 3h4l2 5-3 2a12 12 0 0 0 6 6l2-3 5 2v4a2 2 0 0 1-2 2A18 18 0 0 1 3 5a2 2 0 0 1 2-2z"/></svg>
      <div><b>CONTACT PHONE</b><small>555-210-0148</small></div>
    </div>
    <div class="cblock">
      <svg viewBox="0 0 24 24" fill="none" stroke="#999" stroke-width="1.6"><rect x="3" y="9" width="18" height="10" rx="1"/><path d="M7 9V4h10v5M7 14h10"/></svg>
      <div><b>Fax</b><small>555-210-0172</small></div>
    </div>
    <div class="cblock">
      <svg viewBox="0 0 24 24" fill="none" stroke="#999" stroke-width="1.6"><circle cx="12" cy="12" r="9"/><path d="M12 7v5l3 2"/></svg>
      <div><b>OPEN HOURS</b><small>Mon - Fri 7:00 - 17:00<br>Saturday: 7:00 - 12:00</small></div>
    </div>
  </div>

  <nav class="abs nav">
    <a class="current">Home</a><a>About Us</a><a>Services</a><a>Gallery</a><a>Contact Us</a>
    <span class="social"><i></i><i></i><i></i></span>
  </nav>
</header>

<section class="abs hero" role="img" aria-label="Photo of a large beige metal-roofed barn home with green lawn under a cloudy sky"></section>
<h1 class="abs" style="left:0;width:1200px;top:386px;text-align:center;color:#fff;font-size:42px;font-weight:700;line-height:.95">we will help you to fix<br>your roof</h1>
<div class="abs btn btn-red">Learn More</div>
<div class="abs btn btn-line">Contact Us</div>
<div class="abs slider-nav">
  <svg width="16" height="10" viewBox="0 0 16 10"><path d="M2 8l6-6 6 6" stroke="#111" stroke-width="2.5" fill="none"/></svg>
  <i></i><i></i><i class="on"></i><i></i>
  <svg width="16" height="10" viewBox="0 0 16 10"><path d="M2 2l6 6 6-6" stroke="#111" stroke-width="2.5" fill="none"/></svg>
</div>

<section class="roofing">
  <div class="abs worker" role="img" aria-label="Photo of a roofing contractor in a yellow hard hat with arms crossed"></div>
  <h2 class="abs roofing-title">We Provide Roofing</h2>
  <span class="abs roofing-rule"></span><span class="abs roofing-dots"></span>
  <p class="abs roofing-sub">To numerous customers like government, homes and workplaces</p>

  <div class="abs service" style="left:225px">
    <svg viewBox="0 0 52 48" fill="var(--red)"><path d="M26 4 3 24h6v20h13V32h8v12h13V24h6z"/></svg>
    <p>Complet e Post Frame</p>
  </div>
  <div class="abs service" style="left:411px">
    <svg viewBox="0 0 52 48" fill="none" stroke="var(--red)" stroke-width="2.5"><path d="M8 44V6h12v38M20 44V16h10v28M30 44V24h10v20M4 44h44M12 12h4M12 20h4M12 28h4M24 22h2M24 30h2M34 30h2"/></svg>
    <p>Residential</p>
  </div>
  <div class="abs service" style="left:590px">
    <svg viewBox="0 0 52 48" fill="none" stroke="var(--red)" stroke-width="2.5"><path d="M4 38 20 12h16l12 26zM12 38l14-22M20 38l12-22M28 38l10-20M36 38l6-14M2 40h48"/></svg>
    <p>Prefab Sheets</p>
  </div>
  <div class="abs service" style="left:794px">
    <svg viewBox="0 0 52 48" fill="none" stroke="var(--red)" stroke-width="2.5"><path d="M6 44V22l20-14 20 14v22zM6 30h40M6 37h40M14 16v-8M26 8v-6M38 16v-8M16 44V30M26 44V30M36 44V30"/></svg>
    <p>Agricultrural &amp; Commercial</p>
  </div>
</section>

<section class="abs callband">
  <p class="abs">Get a Professional Services, Call us Now.</p>
  <p class="abs num">555-210-0148</p>
</section>

<section class="gallery">
  <h2 class="abs section-title gallery-title">Our <em>Gallery</em></h2>
  <div class="abs tabs"><span class="on">All Projects</span><span>Post Frame</span><span>Residential</span><span>Prefab Sheet</span><span>Commercial</span></div>
  <div class="abs shots">
    <div class="shot shot-1" role="img" aria-label="Photo of a tan shed with a dark metal roof on grass"></div>
    <div class="shot shot-2" role="img" aria-label="Photo of a barn-style shed with a brown metal roof"></div>
    <div class="shot shot-3" role="img" aria-label="Photo of long white farm buildings on a muddy lot"></div>
    <div class="shot shot-4" role="img" aria-label="Photo of a cream barn with a red metal roof and cupolas"></div>
  </div>
  <div class="abs pager pager-gallery">
    <svg viewBox="0 0 12 16"><path d="M9 2 3 8l6 6" stroke="#111" stroke-width="2.5" fill="none"/></svg>
    <i></i><i class="on"></i><i></i><i></i>
    <svg viewBox="0 0 12 16"><path d="m3 2 6 6-6 6" stroke="#111" stroke-width="2.5" fill="none"/></svg>
  </div>
</section>

<section class="abs testimonials">
  <h2 class="abs section-title">What Our Customer Says</h2>
  <blockquote class="abs quote" style="left:222px">Lorem Ipsum is simply dummy text of the printing and typesetting industry. Lorem Ipsum has been the industry's standard dummy text ever since the 1500s, when an unknown printer took a galley of type and scrambled it to make a type specimen book.It has survived not only five centuries, but also the leap into electronic typesetting, remaining essentially unchanged.</blockquote>
  <blockquote class="abs quote" style="left:611px">Lorem Ipsum is simply dummy text of the printing and typesetting industry. Lorem Ipsum has been the industry's standard dummy text ever since the 1500s, when an unknown printer took a galley of type and scrambled it to make a type specimen book.It has survived not only five centuries, but also the leap into electronic typesetting, remaining essentially unchanged.</blockquote>
  <div class="abs author" style="left:238px"><span class="avatar" role="img" aria-label="Customer portrait"></span><span><b>Elias Marrow</b> &nbsp;/&nbsp; Test Engineer</span></div>
  <div class="abs author" style="left:627px"><span class="avatar" role="img" aria-label="Customer portrait"></span><span><b>Elias Marrow</b> &nbsp;/&nbsp; Test Engineer</span></div>
  <div class="abs pager pager-quotes">
    <svg viewBox="0 0 12 16"><path d="M9 2 3 8l6 6" stroke="#111" stroke-width="2.5" fill="none"/></svg>
    <i></i><i class="on"></i><i></i><i></i>
    <svg viewBox="0 0 12 16"><path d="m3 2 6 6-6 6" stroke="#111" stroke-width="2.5" fill="none"/></svg>
  </div>
</section>

<footer class="abs footer" role="contentinfo">
  <div class="abs brand-foot"><i></i>DORVANE METAL</div>
  <p class="abs about">The roofing inc. is the leader of roof repair and construction in the country sed diam nonumy eirmod tempor invidunt ut labore and efficient strategy.</p>
  <div class="abs fcol fcol-touch">
    <h4>Get In Touch</h4>
    <p>PHONE: +1 555 010 2233<br>FAX: +1 555 010 2244<br>EMAIL: info@dorvanemetal.com</p>
  </div>
  <div class="abs fcol fcol-hours">
    <h4>Opening Hours</h4>
    <p>Monday to Friday<br>7am - 5pm<br>Saturday<br>7am - 12pm<br>SundayClosed</p>
  </div>
  <div class="abs fcol fcol-news">
    <h4>Newsletter</h4>
    <p>Sign up Your Newsletter</p>
  </div>
  <div class="abs newsletter"><span>Email Address</span><b>Go</b></div>
  <span class="abs rule"></span>
  <p class="abs flinks">Home | About Us | Services | Gallery | Contact Us</p>
  <p class="abs copy">Copyright © 2019 Dorvane Metal Inc. All rights reserved.</p>
</footer>

</body>
</html>
```